Forensic Psychology and Polygraph Needs Clever Catchy Logo

There's a massive trade show coming up and we are looking to debut a new, clever logo for our business cards. We are a private practice that offers psychological evaluations, therapeutic counseling, and polygraphing. Our website is kelvora.net (to get a better idea of the color scheme) and instead of the nature/cuddly image that other psychology organizations like to go for, we are interested in cultivating a business, strength, and professional image.
Attached are some popular logos and designs to get those creative juices flowing! I would like to avoid the brain/psi logo as this has been to death so bonus points definitely for originality.
Target Market(s)
governmental agencies, third party mental health providers, individual private pay clients
Industry/Entity Type
Mental Health
Contact Information for Business Card
One one side will be the logo and company name while on the back will be contact information and provider details (name, position, etc)
Look and feel
Each slider illustrates characteristics of the customer's brand and the style your logo design should communicate.

```html
<!DOCTYPE html>
<html lang="en">
<head>
<meta charset="utf-8">
<title>Halvern &amp; Associates – Business Cards</title>
<link href="https://fonts.googleapis.com/css2?family=Cinzel:wght@400&family=Open+Sans:wght@400;600&display=swap" rel="stylesheet">
<style>
  :root {
    --teal: #16b8bb;
    --plum: #524858;
    --ink: #3f3a44;
    --white: #ffffff;
    --backdrop: #eef0f1;
  }
  * { margin: 0; padding: 0; box-sizing: border-box; }
  html, body { width: 1200px; height: 900px; overflow: hidden; }
  body {
    background: var(--backdrop);
    font-family: "Open Sans", Arial, sans-serif;
    position: relative;
  }
  .card {
    position: absolute;
    width: 620px;
    height: 354px;
    border-radius: 4px;
    overflow: hidden;
    box-shadow: 0 10px 28px rgba(0,0,0,0.18);
  }
  /* Front */
  .card-front {
    left: 110px; top: 110px;
    background: var(--teal);
    color: var(--white);
    text-align: center;
  }
  .brand-dot {
    width: 86px; height: 86px;
    border-radius: 50%;
    background: var(--white);
    margin: 56px auto 18px;
  }
  .brand-name {
    font-family: "Cinzel", Georgia, serif;
    font-weight: 400;
    font-size: 28px;
    letter-spacing: 1px;
    line-height: 1;
  }
  .brand-tagline {
    font-family: "Cinzel", Georgia, serif;
    font-size: 14px;
    letter-spacing: 2px;
    margin-top: 6px;
  }
  .services {
    list-style: none;
    display: flex;
    justify-content: center;
    gap: 28px;
    margin-top: 40px;
    font-size: 16px;
  }
  .services li::before {
    content: "";
    display: inline-block;
    width: 9px; height: 9px;
    border-radius: 50%;
    background: var(--white);
    margin-right: 7px;
    vertical-align: middle;
  }
  /* Back */
  .card-back {
    left: 470px; top: 430px;
    background: var(--white);
  }
  .card-back .wave {
    position: absolute; left: 0; top: 0;
    width: 620px; height: 354px;
  }
  .back-mark {
    position: absolute;
    left: 50px; top: 48px;
    width: 170px;
    text-align: center;
  }
  .back-mark .mark-circle {
    width: 150px; height: 150px;
    border-radius: 50%;
    background: var(--teal);
    margin: 0 auto 10px;
  }
  .back-mark .mark-name {
    font-size: 15px;
    font-weight: 600;
    color: var(--teal);
    letter-spacing: 1px;
  }
  .contact {
    position: absolute;
    left: 330px; top: 30px;
    color: var(--ink);
    font-size: 14px;
    line-height: 1.45;
  }
  .contact .person {
    font-size: 19px;
    font-weight: 600;
    color: var(--teal);
    line-height: 1.1;
  }
  .contact .role { font-size: 14px; margin-bottom: 10px; }
  .contact .line { display: flex; align-items: center; gap: 8px; }
  .contact .line svg { width: 12px; height: 12px; fill: var(--teal); flex: none; }
  .contact .address { margin-top: 8px; padding-left: 20px; }
</style>
</head>
<body>

  <section class="card card-front" aria-label="Business card front">
    <div class="brand-dot"></div>
    <h1 class="brand-name">Halvern &amp; Associates</h1>
    <p class="brand-tagline">PSYCHOLOGICAL SERVICES</p>
    <ul class="services">
      <li>Therapy</li>
      <li>Evaluations</li>
      <li>Consultation</li>
    </ul>
  </section>

  <section class="card card-back" aria-label="Business card back">
    <svg class="wave" viewBox="0 0 620 354" preserveAspectRatio="none" aria-hidden="true">
      <path d="M0 332 C 190 322, 360 262, 470 228 C 535 210, 585 206, 620 206 L620 354 L0 354 Z" fill="var(--teal)"/>
      <path d="M0 292 C 140 255, 320 250, 470 220 C 350 262, 170 280, 0 322 Z" fill="var(--plum)"/>
    </svg>

    <div class="back-mark">
      <div class="mark-circle"></div>
      <div class="mark-name">HALVERN</div>
    </div>

    <div class="contact">
      <p class="person">DANIEL MERCER</p>
      <p class="role">Managing Director</p>
      <p class="line">
        <svg viewBox="0 0 24 24"><path d="M6.6 10.8a15 15 0 0 0 6.6 6.6l2.2-2.2a1 1 0 0 1 1-.25 11.4 11.4 0 0 0 3.6.6 1 1 0 0 1 1 1V20a1 1 0 0 1-1 1A17 17 0 0 1 3 4a1 1 0 0 1 1-1h3.5a1 1 0 0 1 1 1c0 1.25.2 2.45.6 3.6a1 1 0 0 1-.25 1z"/></svg>
        555.014.2230
      </p>
      <p class="line">
        <svg viewBox="0 0 24 24"><path d="M2 5h20v14H2z M2 5l10 8 10-8" stroke="#fff" stroke-width="1.5"/></svg>
        contact@kelvora.net
      </p>
      <p class="address">2280 W. Alder Crest Rd.<br>Suites 204 and 208 Tempe,<br>Arizona 85280</p>
    </div>
  </section>

</body>
</html>
```